Australian residential property business needs a business card design

I need a business card design for my new business 'Harbour Estate Ventures'. The business will involve house purchases, land development sites, renovation projects, sub-divisions etc. I will be buying property from motivated vendors and working with property investors. I will deal with a wide range of people working in the residential property market including real estate agents, councils, tradespeople, banks, home owners, etc.

I would like something simple, not flashy, but a little bit unique. The colours should be in line with my logo. The business card needs to be professional. I would like something memorable, but not 'busy' or too bright. Not boring. Modern ok.

Target Market(s)

Home owners looking to sell their property, real estate agents, tradespeople (e.g. plumbers, builders, electricians etc), property investors, local councils, and anyone else involved in the residential property industry

Industry/Entity Type

Business

Contact Information for Business Card

I need to include my business name/logo, my name, my title, a PO Box number/address, a mobile number, and an email address.

Font styles to use
Serif

Requirements
Must have
• My business card details listed above.

```html
<!DOCTYPE html>
<html lang="en">
<head>
<meta charset="utf-8">
<title>Harbour Estate Ventures – Business Card</title>
<link rel="stylesheet" href="https://fonts.googleapis.com/css2?family=Open+Sans:wght@400;600;700&display=swap">
<style>
  :root {
    --green: #008f45;
    --orange-light: #f8b62c;
    --orange: #f08a1e;
    --white: #ffffff;
    --backdrop: #d9d9d9;
    --brand-orange: #f29a1f;
  }
  * { margin: 0; padding: 0; box-sizing: border-box; }
  html, body {
    width: 1200px; height: 900px; overflow: hidden;
    background: var(--backdrop);
    font-family: "Open Sans", Arial, sans-serif;
  }
  .card {
    position: absolute; left: 250px;
    width: 700px; height: 400px;
    overflow: hidden;
    box-shadow: 0 4px 14px rgba(0,0,0,0.18);
  }
  .card--front { top: 30px; background: var(--white); }
  .card--back  { top: 470px; background: var(--green); }
  .card__shapes { position: absolute; inset: 0; width: 700px; height: 400px; }

  .brand {
    position: absolute;
    display: flex; align-items: center; gap: 10px;
    font-weight: 700; font-size: 26px; letter-spacing: 0.5px;
    white-space: nowrap;
  }
  .brand__dot { width: 16px; height: 16px; border-radius: 50%; flex: none; }
  .card--front .brand { left: 50px; top: 70px; color: var(--brand-orange); }
  .card--front .brand__dot { background: var(--green); }
  .card--back .brand { right: 50px; top: 188px; color: var(--white); }
  .card--back .brand__dot { background: var(--orange-light); }

  .holder {
    position: absolute; right: 45px; top: 222px;
    text-align: right; color: var(--white);
  }
  .holder__name { font-size: 30px; font-weight: 600; line-height: 1.2; }
  .holder__title { font-size: 18px; font-weight: 400; line-height: 1.3; }

  .contact {
    position: absolute; left: 44px; top: 232px;
    list-style: none; color: var(--white);
    font-size: 17px; line-height: 31px;
  }
  .contact li { display: flex; align-items: center; gap: 9px; }
  .contact svg { width: 13px; height: 13px; fill: var(--white); flex: none; }
</style>
</head>
<body>

<section class="card card--front" aria-label="Business card front">
  <svg class="card__shapes" viewBox="0 0 700 400" aria-hidden="true">
    <defs>
      <linearGradient id="orangeFade" x1="0" y1="0" x2="0" y2="1">
        <stop offset="0" stop-color="#f8b62c"/>
        <stop offset="1" stop-color="#f08a1e"/>
      </linearGradient>
    </defs>
    <polygon points="0,142 700,208 700,400 0,400" fill="url(#orangeFade)"/>
    <polygon points="0,142 700,208 700,352 0,160" fill="#008f45"/>
  </svg>

  <div class="brand"><span class="brand__dot"></span>HARBOUR ESTATE VENTURES</div>

  <div class="holder">
    <p class="holder__name">Daniel Mercer</p>
    <p class="holder__title">Managing Director</p>
  </div>

  <ul class="contact">
    <li>
      <svg viewBox="0 0 16 16"><path d="M3 1l3 3-2 2c1 2 3 4 6 6l2-2 3 3-2 2C7 15 1 9 1 3z"/></svg>
      123.456.7890
    </li>
    <li>
      <svg viewBox="0 0 16 16"><path d="M1 3h14v10H1z M1 3l7 6 7-6" fill="#fff" stroke="#f3a023" stroke-width="1.2"/></svg>
      hello@harbourestate.com
    </li>
    <li>
      <svg viewBox="0 0 16 16"><path d="M8 0a5 5 0 0 1 5 5c0 4-5 11-5 11S3 9 3 5a5 5 0 0 1 5-5zm0 3a2 2 0 1 0 0 4 2 2 0 0 0 0-4z"/></svg>
      1234, Address Goes Here, Country Name, 123456
    </li>
  </ul>
</section>

<section class="card card--back" aria-label="Business card back">
  <svg class="card__shapes" viewBox="0 0 700 400" aria-hidden="true">
    <defs>
      <linearGradient id="orangeFadeBack" x1="0" y1="0" x2="0" y2="1">
        <stop offset="0" stop-color="#f8b62c"/>
        <stop offset="1" stop-color="#f08a1e"/>
      </linearGradient>
    </defs>
    <polygon points="0,140 700,212 700,350 0,160" fill="url(#orangeFadeBack)"/>
  </svg>

  <div class="brand"><span class="brand__dot"></span>HARBOUR ESTATE VENTURES</div>
</section>

</body>
</html>
```